Sole trader requires buisness card / company logo for mining and aviation

I require a business card and logo design having the following requirements;
Skyward and Engine Works
Owner: Martin Hollis
Ph: 0471593064
E: martin-r-hollis@quillmail.com.au

Logo should include a basic aircraft image and an image of an item of mining machinery either a dump truck or large excavator, but keeping in mind that the image is to be transferred onto clothing embroidery.

```html
<!DOCTYPE html>
<html lang="en">
<head>
<meta charset="utf-8">
<title>Skyward and Engine Works – Business Card</title>
<link rel="stylesheet" href="https://fonts.googleapis.com/css2?family=Michroma&display=swap">
<style>
  :root {
    --backdrop: #e4e4e6;
    --card: #ffffff;
    --ink: #3c3c40;
    --ink-soft: #55565b;
    --brand-blue: #1a8fd6;
    --brand-blue-light: #19a7e6;
    --brand-blue-deep: #2c5cb8;
    --swoosh-grey: #6b6c70;
    --on-blue: #ffffff;
  }
  * { box-sizing: border-box; margin: 0; padding: 0; }
  html, body {
    width: 1200px; height: 900px; overflow: hidden;
    background: var(--backdrop);
    font-family: "Michroma", "Helvetica Neue", Arial, sans-serif;
  }
  .card {
    position: absolute; left: 120px; top: 176px;
    width: 960px; height: 548px;
    background: var(--card);
    box-shadow: 0 18px 40px rgba(0,0,0,.18);
    overflow: hidden;
  }
  .card__wave { position: absolute; inset: 0; }
  .brand {
    position: absolute; left: 70px; top: 150px;
    display: flex; align-items: center; gap: 22px;
  }
  .brand__dot {
    width: 86px; height: 86px; border-radius: 50%;
    background: var(--brand-blue);
    flex: none;
  }
  .brand__name {
    color: var(--brand-blue);
    font-size: 20px; line-height: 1.4; letter-spacing: .5px;
  }
  .holder {
    position: absolute; right: 350px; top: 48px; text-align: right;
    color: var(--ink);
    white-space: nowrap;
  }
  .holder__name { font-size: 22px; letter-spacing: 2px; text-transform: uppercase; }
  .holder__role { font-size: 12px; letter-spacing: 2px; text-transform: uppercase; margin-top: 8px; }
  .address {
    position: absolute; right: 36px; top: 150px; text-align: right;
    color: var(--on-blue); font-size: 18px; line-height: 1.55; letter-spacing: .5px;
    white-space: nowrap;
  }
  .contacts {
    position: absolute; left: 80px; top: 320px;
    list-style: none; color: var(--ink-soft); font-size: 12px;
  }
  .contacts li { display: flex; align-items: center; gap: 12px; height: 32px; white-space: nowrap; }
  .contacts svg { width: 15px; height: 15px; fill: var(--ink-soft); flex: none; }
  .contacts .icon-globe { fill: none; stroke: var(--ink-soft); stroke-width: 1.4; }
</style>
</head>
<body>
  <section class="card" aria-label="Skyward and Engine Works business card">
    <svg class="card__wave" viewBox="0 0 960 548" aria-hidden="true">
      <defs>
        <linearGradient id="band" x1="0" y1="1" x2="1" y2="0">
          <stop offset="0" stop-color="#2c5cb8"/>
          <stop offset=".5" stop-color="#1a8fd6"/>
          <stop offset="1" stop-color="#19a7e6"/>
        </linearGradient>
      </defs>
      <path d="M320 548 C500 480 570 380 590 260 C605 160 620 60 660 0"
            fill="none" stroke="#6b6c70" stroke-width="9"/>
      <path d="M360 548 C540 480 610 380 630 260 C645 160 660 60 700 0 L960 0 L960 548 Z"
            fill="url(#band)"/>
    </svg>

    <div class="brand">
      <span class="brand__dot"></span>
      <p class="brand__name">Skyward and<br>Engine Works</p>
    </div>

    <div class="holder">
      <p class="holder__name">Martin Hollis</p>
      <p class="holder__role">Financial Advisor</p>
    </div>

    <p class="address">214.6th floor.Quay<br>Kestrel Road KTH</p>

    <ul class="contacts">
      <li><svg viewBox="0 0 16 16"><path d="M4 1l3 3-2 2c1 2 3 4 5 5l2-2 3 3-2 3C7 15 1 9 1 3z"/></svg>0471593064</li>
      <li><svg viewBox="0 0 16 16"><path d="M4 0h8v16H4zM5 2v10h6V2z"/></svg>0471593064</li>
      <li><svg viewBox="0 0 16 16"><path d="M3 0h7l3 3v13H3zM5 6h6v1H5zm0 3h6v1H5zm0 3h6v1H5z"/></svg>0471593064</li>
      <li><svg viewBox="0 0 16 16"><path d="M0 3h16v10H0zM1 4l7 5 7-5v-0.5H1z"/></svg>martin-r-hollis@quillmail.com.au</li>
      <li><svg class="icon-globe" viewBox="0 0 16 16"><circle cx="8" cy="8" r="6.8"/><ellipse cx="8" cy="8" rx="3" ry="6.8"/><path d="M1.2 8h13.6"/></svg>www.skywardengine.com.au</li>
    </ul>
  </section>
</body>
</html>
```